Structural Engineering Business Card

Veltrow Drafts does residential house plans for clients in Central Florida. Would like simple but elegant business card that is appropriate for a house plan engineering company. Prefer black business card with black/white them but open to other shades of blue. I uploaded a sample card that I came across that looked good but please come up with your own creative designs.

Contact Information for Business Card

Name, Title, Phone, Email, Address, website

```html
<!DOCTYPE html>
<html lang="en">
<head>
<meta charset="utf-8">
<title>Veltrow Drafts – Business Card</title>
<link rel="stylesheet" href="https://fonts.googleapis.com/css2?family=Arimo:wght@400;700&display=swap">
<style>
  :root {
    --backdrop: #d6d6d6;
    --card-white: #ffffff;
    --card-black: #161616;
    --ink: #111111;
    --ink-soft: #2a2a2a;
    --paper-text: #ffffff;
  }
  * { margin: 0; padding: 0; box-sizing: border-box; }
  html, body {
    width: 1200px; height: 800px; overflow: hidden;
    background: var(--backdrop);
    font-family: "Arimo", Arial, sans-serif;
  }
  .canvas {
    width: 1200px; height: 800px;
    display: flex; align-items: center; justify-content: center; gap: 50px;
  }
  .card {
    position: relative;
    width: 525px; height: 300px;
    border-radius: 22px;
    overflow: hidden;
    box-shadow: 0 10px 26px rgba(0,0,0,0.18);
  }
  .card--front { background: var(--card-white); color: var(--ink); }
  .card--back { background: var(--card-black); color: var(--paper-text); }

  .state-silhouette {
    position: absolute; top: 0; right: 0;
    width: 385px; height: 100px;
    background: var(--ink);
    border-radius: 0 0 0 48px;
  }

  .contact {
    position: absolute; left: 34px; top: 122px;
    font-size: 12px; line-height: 1.3; color: var(--ink-soft);
  }
  .contact__name {
    font-size: 17px; font-weight: 700; letter-spacing: 0.4px;
    color: var(--ink); text-transform: uppercase;
  }
  .contact__title { margin-bottom: 6px; }
  .contact__address { margin-bottom: 6px; }
  .contact__row { display: flex; align-items: center; gap: 8px; }
  .contact__icon { width: 12px; height: 12px; flex: none; }
  .contact__web { padding-left: 20px; }

  .brand {
    position: absolute; inset: 0;
    display: flex; align-items: center; justify-content: center; gap: 14px;
  }
  .brand__mark { width: 22px; height: 22px; background: var(--paper-text); flex: none; }
  .brand__name {
    font-size: 38px; font-weight: 700; letter-spacing: 1px;
    text-transform: uppercase; color: var(--paper-text); white-space: nowrap;
  }
</style>
</head>
<body>
<main class="canvas">
  <section class="card card--front">
    <div class="state-silhouette" role="img" aria-label="Solid black silhouette map of the state of Florida"></div>
    <div class="contact">
      <p class="contact__name">Marcus Hale</p>
      <p class="contact__title">Managing Director</p>
      <p class="contact__address">4120 Cedar Hollow Lane<br>Kissimmee, Florida 34741</p>
      <p class="contact__row">
        <svg class="contact__icon" viewBox="0 0 12 12" aria-hidden="true"><path d="M2.5 1 L4.5 1 L5.2 3.6 L4 4.6 Q5 7 7.4 8 L8.4 6.8 L11 7.5 L11 9.5 Q10 11 8 11 Q1 9 1 2.5 Q1 1 2.5 1Z" fill="#111"/></svg>
        <span>407-555-0182</span>
      </p>
      <p class="contact__row">
        <svg class="contact__icon" viewBox="0 0 12 12" aria-hidden="true"><rect x="2.5" y="0.8" width="7" height="10.4" rx="1" fill="none" stroke="#111" stroke-width="1.3"/></svg>
        <span>407-555-0147</span>
      </p>
      <p class="contact__row">
        <svg class="contact__icon" viewBox="0 0 12 12" aria-hidden="true"><rect x="0.5" y="2" width="11" height="8" fill="#111"/><path d="M0.5 2 L6 6.5 L11.5 2" fill="none" stroke="#fff" stroke-width="1"/></svg>
        <span>info@veltrowdrafts.com</span>
      </p>
      <p class="contact__web">www.veltrowdrafts.com</p>
    </div>
  </section>

  <section class="card card--back">
    <div class="brand">
      <span class="brand__mark"></span>
      <span class="brand__name">Veltrow Drafts</span>
    </div>
  </section>
</main>
</body>
</html>
```